Building certification business in Sydney Australia

Brookvale Assessors is a small business that is currently growing and needs a profession looking website to attract customers and give them all the information they need. The main services we offer currently are pre-purchase building inspections for purchasers and other areas of construction consultancy including pool fencing certificates. Please see attached logos to incorporate to also match colour schemes with. Thanks!

Target Market(s)

Prospective buyers and home owners

Industry/Entity Type

Small Business

Requirements
Must have
• Promote the main services from the home page. Being able to select the type of service/certificate required from the main page and be directed to a specific page that deals with only that service containing the relevant information for that item.
Nice to have
• Small emphasis on the location of our office and areas we service etc.

```html
<!DOCTYPE html>
<html lang="en">
<head>
<meta charset="utf-8">
<title>Brookvale Assessors</title>
<link rel="stylesheet" href="https://fonts.googleapis.com/css2?family=PT+Sans:ital,wght@0,400;0,700;1,400&family=PT+Sans+Narrow:wght@700&family=Arimo&display=swap">
<style>
:root{
  --blue:#2a84c6;
  --blue-dark:#1e6fae;
  --navy:#1f3a56;
  --ink:#333;
  --muted:#666;
  --band:#f1f1f1;
  --white:#fff;
  --footer:#2b2b2b;
  --line:#dcdcdc;
}
*{box-sizing:border-box;margin:0;padding:0}
html,body{width:782px;height:1200px;overflow:hidden;background:var(--white)}
body{position:relative;font-family:"PT Sans",sans-serif;color:var(--ink)}
.abs{position:absolute}

/* header */
.site-header{position:absolute;left:0;top:0;width:782px;height:89px;background:var(--white)}
.brand{position:absolute;left:57px;top:29px}
.brand-name{font-size:24px;font-weight:700;color:var(--navy);letter-spacing:-.2px}
.main-nav{position:absolute;left:330px;top:0;display:flex}
.nav-item{width:76px;height:89px;text-align:center;padding-top:30px;margin-right:9px}
.nav-item .label{display:block;font-size:12px;color:var(--ink)}
.nav-item .sub{display:block;font-size:9.5px;font-style:italic;color:#888;margin-top:3px}
.nav-item.active{background:var(--blue)}
.nav-item.active .label,.nav-item.active .sub{color:var(--white)}

/* hero */
.hero{position:absolute;left:0;top:89px;width:782px;height:313px;
  background:linear-gradient(180deg,#b9b3a7 0%,#a59d8c 35%,#7f9a55 70%,#5f8a3a 100%)}
.hero-sheen{position:absolute;left:0;top:0;width:420px;height:313px;
  background:linear-gradient(120deg,rgba(255,255,255,.35),rgba(255,255,255,0) 70%)}
.hero-card{position:absolute;left:174px;top:46px;width:217px;height:222px;background:var(--white);overflow:hidden}
.hero-card .corner{position:absolute;width:0;height:0}
.corner.tr{right:0;top:0;border-top:40px solid var(--blue);border-left:40px solid transparent}
.corner.bl{left:0;bottom:0;border-bottom:42px solid var(--blue);border-right:42px solid transparent}
.hero-title{position:absolute;left:17px;top:40px;font-family:"PT Sans Narrow",sans-serif;font-size:21px;color:var(--blue-dark);letter-spacing:.3px}
.hero-sub{position:absolute;left:17px;top:71px;font-size:15px;color:#555;letter-spacing:.3px}
.hero-text{position:absolute;left:17px;top:96px;width:195px;font-size:10.5px;line-height:16px;color:var(--muted)}
.btn{position:absolute;left:17px;top:155px;width:87px;height:22px;background:var(--blue);color:var(--white);font-size:11px;text-align:center;line-height:22px}
.slider-dots{position:absolute;left:667px;top:288px;display:flex;gap:3px}
.slider-dots span{width:11px;height:11px;border-radius:50%;background:rgba(255,255,255,.55)}
.slider-dots span:first-child{background:var(--white)}

/* services */
.card{position:absolute;width:200px;background:var(--white);border:1px solid var(--line)}
.card::after{content:"";position:absolute;left:20px;right:-6px;bottom:-7px;height:6px;
  background:radial-gradient(ellipse at 60% 0,rgba(0,0,0,.35),rgba(0,0,0,0) 70%)}
.card-media{margin:4px;height:98px}
.service{height:187px}
.service .card-title{font-size:12px;font-weight:400;color:var(--blue-dark);padding:12px 7px 5px}
.service .card-text{font-size:9px;line-height:15px;color:var(--muted);padding:0 6px;letter-spacing:-.1px}

/* projects band */
.projects{position:absolute;left:0;top:697px;width:782px;height:330px;background:var(--band)}
.projects::after{content:"";position:absolute;left:0;right:0;bottom:-14px;height:14px;
  background:radial-gradient(ellipse at 50% 0,rgba(0,0,0,.08),rgba(0,0,0,0) 70%)}
.tab{position:absolute;left:312px;top:-9px;width:176px;height:38px}
.tab-body{position:absolute;left:8px;top:8px;width:160px;height:30px;background:var(--blue);color:var(--white);
  font-size:14px;font-weight:400;text-align:center;line-height:28px}
.section-intro{position:absolute;left:50px;top:48px;width:682px;text-align:center;font-size:9.5px;line-height:15px;color:var(--muted)}
.project{height:182px}
.project .card-media{height:110px}
.project .card-title{font-size:12px;font-weight:400;color:var(--blue-dark);text-align:center;padding:12px 0 6px}
.project .card-text{font-size:9.5px;color:var(--muted);text-align:center}
.project.active{border-bottom:2px solid var(--blue)}

/* contact strip */
.contact-strip{position:absolute;left:0;top:1050px;width:782px;height:60px}
.contact-item{position:absolute;display:flex;align-items:center;gap:14px}
.contact-item .main{font-size:11px;color:#444}
.contact-item .note{font-size:9.5px;color:#777;margin-top:4px}
.divider{position:absolute;top:10px;width:1px;height:30px;background:#cfcfcf}

/* footer */
.site-footer{position:absolute;left:0;top:1113px;width:782px;height:87px;background:var(--footer);color:var(--white);font-family:"Arimo",sans-serif}
.footer-links{position:absolute;left:57px;top:20px;font-size:9.5px}
.copyright{position:absolute;left:57px;top:44px;font-size:9.5px}
.social{position:absolute;left:571px;top:27px;display:flex;gap:9px}
.social span{width:23px;height:23px}
</style>
</head>
<body>

<header class="site-header">
  <div class="brand"><span class="brand-name">Brookvale Assessors</span></div>
  <nav class="main-nav">
    <div class="nav-item active"><span class="label">HOME</span><span class="sub">all starts here</span></div>
    <div class="nav-item"><span class="label">ABOUT US</span><span class="sub">adipiscing</span></div>
    <div class="nav-item"><span class="label">SERVICES</span><span class="sub">Aenean masa</span></div>
    <div class="nav-item"><span class="label">PROJECTS</span><span class="sub">commodgula</span></div>
    <div class="nav-item"><span class="label">CONTACT</span><span class="sub">sit amet</span></div>
  </nav>
</header>

<section class="hero" role="img" aria-label="Photo of a smiling family standing on the lawn in front of a brick house">
  <div class="hero-sheen"></div>
  <div class="hero-card">
    <span class="corner tr"></span><span class="corner bl"></span>
    <h1 class="hero-title">THE DAYS OF BUYING</h1>
    <p class="hero-sub">DON'T BUY ANYMOSERVICE</p>
    <p class="hero-text">Jerta baditaut onsequser untur magni dol ores eoquie voluptate msequi nesciunt. Voluptatem accusantium dolorem.</p>
    <span class="btn">READ MORE</span>
  </div>
  <div class="slider-dots"><span></span><span></span><span></span><span></span></div>
</section>

<section class="services">
  <article class="card service" style="left:56px;top:450px">
    <div class="card-media" role="img" aria-label="Illustration of a house beside an energy rating scale" style="background:linear-gradient(90deg,#5aa64a,#e8e050 55%,#e14b2d)"></div>
    <h2 class="card-title">Pre-purchase building inspections</h2>
    <p class="card-text">Claritas est etiam processus dynamicus, qui se quitur mutationem consuetudium lectorum.</p>
  </article>
  <article class="card service" style="left:289px;top:450px">
    <div class="card-media" role="img" aria-label="Photo of a fenced swimming pool with timber decking" style="background:linear-gradient(160deg,#6a7880,#3aa0c8 45%,#d8cdb8 70%,#8a4a2c)"></div>
    <h2 class="card-title">Pool fencing certificates</h2>
    <p class="card-text">Claritas est etiam processus dynamicus, qui se quitur mutationem consuetudium lectorum.</p>
  </article>
  <article class="card service" style="left:521px;top:450px">
    <div class="card-media" role="img" aria-label="Photo of building plans, glasses and a hard hat on a desk" style="background:linear-gradient(180deg,#c9d4dc,#e8ecef 60%,#d6c470)"></div>
    <h2 class="card-title">Pool fencing certificates</h2>
    <p class="card-text">Claritas est etiam processus dynamicus, qui se quitur mutationem consuetudium lectorum.</p>
  </article>
</section>

<section class="projects">
  <div class="tab">
    <svg class="abs" width="176" height="8" viewBox="0 0 176 8" style="left:0;top:0"><polygon points="0,8 8,0 8,8" fill="#1a5f96"/><polygon points="168,0 176,8 168,8" fill="#1a5f96"/><rect x="8" y="0" width="160" height="8" fill="#2a84c6"/></svg>
    <h2 class="tab-body">Latest Projects</h2>
  </div>
  <p class="section-intro">Mirum est notare quam littera gothica, quam nunc putamus parum claram, anteposuerit litterarum formas humanitatis per seacula quarta decima et quinta decima. Eodem modo typi, qui nunc nobis videntur parum clari, fiant sollemnes in futurum. Mirum est notare quam littera gothica, quam nunc putamus parum .</p>

  <article class="card project active" style="left:56px;top:103px">
    <div class="card-media" role="img" aria-label="Photo of a farmhouse with a white fence and silo" style="background:linear-gradient(180deg,#8a96a0,#c7cfd3 45%,#5f7d46 80%)"></div>
    <h3 class="card-title">DONEC NEC JUSTO EGE FS</h3>
    <p class="card-text">Donec nec justo eget felis facilisis fermtum .</p>
  </article>
  <article class="card project" style="left:289px;top:103px">
    <div class="card-media" role="img" aria-label="Photo of a suburban house with a double garage" style="background:linear-gradient(180deg,#4f86c6,#b9c9d6 45%,#c9b79a 65%,#6f8f4a)"></div>
    <h3 class="card-title">DONEC NEC JUSTO EGE FS</h3>
    <p class="card-text">Donec nec justo eget felis facilisis fermtum .</p>
  </article>
  <article class="card project" style="left:521px;top:103px">
    <div class="card-media" role="img" aria-label="Photo of hands holding house keys and a small model house" style="background:linear-gradient(90deg,#e9e9e9,#d7c2b2 50%,#e6e6e6)"></div>
    <h3 class="card-title">DONEC NEC JUSTO EGE FS</h3>
    <p class="card-text">Donec nec justo eget felis facilisis fermtum .</p>
  </article>
</section>

<section class="contact-strip">
  <div class="contact-item" style="left:57px;top:8px">
    <svg width="18" height="24" viewBox="0 0 18 24"><path d="M9 0C4 0 0 4 0 9c0 6 9 15 9 15s9-9 9-15c0-5-4-9-9-9z" fill="#444"/><circle cx="9" cy="9" r="3.5" fill="#fff"/></svg>
    <div><p class="main">Duis autem vel eum iriureHendrerit.</p><p class="note">Typi non habent claritatem insitam</p></div>
  </div>
  <span class="divider" style="left:298px"></span>
  <div class="contact-item" style="left:353px;top:12px">
    <svg width="18" height="20" viewBox="0 0 18 20"><path d="M4 0l4 5-2 3c1 3 3 5 6 6l3-2 3 4-3 4C7 19 0 11 1 3z" fill="#444"/></svg>
    <p class="main">123 - 456 - 789</p>
  </div>
  <span class="divider" style="left:503px"></span>
  <div class="contact-item" style="left:556px;top:12px">
    <svg width="30" height="18" viewBox="0 0 30 18"><rect width="30" height="18" fill="#444"/><path d="M0 0l15 10L30 0" fill="none" stroke="#fff" stroke-width="1.5"/></svg>
    <p class="main">info@brookvalemail.com</p>
  </div>
</section>

<footer class="site-footer">
  <p class="footer-links">Terms and Conditions | Privacy Promise | FAQ's | Contact Us</p>
  <p class="copyright">Copyright © 2013. All Rights Reserved.</p>
  <div class="social" aria-label="Social links">
    <span style="background:#3b5a9a"></span>
    <span style="background:#2a9bd6"></span>
    <span style="background:#f07a1e"></span>
    <span style="background:#d9302c"></span>
  </div>
</footer>

</body>
</html>
```